PLOV Crossway Summit Poster

We are a cellular therapy (bone marrow transplants, etc) accreditation foundation who needs a poster design for a small workshop that we are going to host within a large workshop. The workshop will 1) Educate doctors who inspect program trying to get accredited. 2) Educate programs on how to become accredited.

It will be printed and mounted on foam board for display at the PLOV booth in exhibition halls. Dimensions should be 11 x 17 inches.

Our website is www.plovsite-example.org. The design does not have to have the same theme/colors as our website.

The poster should have written:

Cellular Therapy Inspection and Accreditation Workshop
February 10th, 2015
Orvell Crossway Summit
San Diego, CA

The statement below should be in small, subtle text to allow room for the other information. All returns, italics, and trademark symbols must be used exactly as included below:

The Halvering Institute of Health Sciences, Office for Ongoing Learning is accredited by the Certification Board for Ongoing Clinical Training to provide continuing medical education for physicians.

The Halvering Institute of Health Sciences, Office for Ongoing Learning designates this live activity for a maximum of 7.5 QLB VRX Tier 1 Unit(s)™. Physicians should claim only credit commensurate with the extent of their participation in the activity.

It should also have our logo on it (I have attached 2, use the one that has the best resolution)

Let me know if there are any questions!

```html
<!DOCTYPE html>
<html lang="en">
<head>
<meta charset="utf-8">
<title>PLOV Crossway Summit Poster</title>
<link href="https://fonts.googleapis.com/css2?family=Signika:wght@400;600&display=swap" rel="stylesheet">
<style>
  :root {
    --paper: #e3e3e3;
    --band: #7a7a7a;
    --base: #767676;
    --shadow: #575757;
    --red: #e3171f;
    --ink: #555555;
    --soft-white: #f2f2f2;
  }
  * { margin: 0; padding: 0; box-sizing: border-box; }
  html, body { width: 770px; height: 1200px; overflow: hidden; background: #ffffff; }
  .poster {
    position: relative;
    width: 770px;
    height: 1200px;
    background: var(--paper);
    font-family: "Signika", Arial, sans-serif;
    overflow: hidden;
  }
  .backdrop { position: absolute; inset: 0; }
  .brand { position: absolute; left: 66px; top: 56px; display: flex; align-items: flex-start; gap: 14px; }
  .brand-name {
    color: var(--red);
    font-size: 80px;
    font-weight: 400;
    line-height: 1;
    letter-spacing: -1px;
  }
  .brand-full {
    margin-top: 46px;
    color: var(--ink);
    font-size: 15.5px;
    line-height: 1.08;
    text-transform: uppercase;
  }
  .brand-home {
    position: absolute;
    left: 68px;
    top: 165px;
    color: var(--ink);
    font-size: 12.5px;
    text-transform: uppercase;
  }
  .headline {
    position: absolute;
    left: 68px;
    top: 222px;
    color: var(--red);
    font-size: 33px;
    font-weight: 600;
    line-height: 1.33;
  }
  .event-details {
    position: absolute;
    left: 68px;
    top: 320px;
    color: var(--ink);
    font-size: 19.5px;
    line-height: 24px;
  }
  .fine-print {
    position: absolute;
    left: 68px;
    top: 998px;
    width: 288px;
    color: var(--soft-white);
    font-size: 10px;
    line-height: 15px;
    text-align: justify;
  }
  .fine-print p + p { margin-top: 14px; }
  .divider {
    position: absolute;
    left: 373px;
    top: 992px;
    width: 1px;
    height: 168px;
    background: #a8a8a8;
  }
  .contact {
    position: absolute;
    left: 392px;
    top: 998px;
    width: 315px;
    color: var(--soft-white);
    font-size: 10px;
    line-height: 15px;
  }
  .contact p + p { margin-top: 14px; }
  .contact .accent { color: var(--red); font-weight: 600; }
</style>
</head>
<body>
<main class="poster">
  <svg class="backdrop" width="770" height="1200" viewBox="0 0 770 1200">
    <defs>
      <radialGradient id="photo-tones" cx="0.38" cy="0.78" r="0.78" fx="0.3" fy="0.8">
        <stop offset="0" stop-color="#4d86c6"/>
        <stop offset="0.35" stop-color="#93b6da"/>
        <stop offset="0.7" stop-color="#e9e4de"/>
        <stop offset="1" stop-color="#e3e3e3"/>
      </radialGradient>
    </defs>
    <rect class="photo-area" x="0" y="415" width="697" height="515" fill="url(#photo-tones)" role="img" aria-label="Photograph: an older couple smiling and shaking hands with a physician in a white coat with a stethoscope"/>
    <rect class="side-band" x="697" y="0" width="73" height="1200" fill="var(--band)"/>
    <path class="curve-shadow" d="M0 925 L430 925 Q640 925 697 660 L697 1200 L0 1200 Z" fill="var(--shadow)"/>
    <path class="curve-base" d="M0 952 L450 952 Q665 952 697 710 L697 1200 L0 1200 Z" fill="var(--base)"/>
  </svg>

  <header class="brand">
    <div class="brand-name">PLOV</div>
    <div class="brand-full">Partnership for the<br>Lab Oversight &amp;<br>Validation</div>
  </header>
  <div class="brand-home">At the Halvering Institute of Health Sciences</div>

  <h1 class="headline">Cellular Therapy Inspection<br>and Accreditation Workshop</h1>

  <div class="event-details">
    <p>February 10th, 2015</p>
    <p>Orvell Crossway Summit</p>
    <p>San Diego, CA</p>
  </div>

  <section class="fine-print">
    <p>The Halvering Institute of Health Sciences, Office for Ongoing Learning is accredited by the Certification Board for Ongoing Clinical Training to provide continuing medical education for physicians.</p>
    <p>The Halvering Institute of Health Sciences, Office for Ongoing Learning designates this live activity for a maximum of 7.5 QLB VRX Tier 1 Unit(s)™. Physicians should claim only credit commensurate with the extent of their participation in the activity.</p>
  </section>

  <div class="divider"></div>

  <section class="contact">
    <p>Partnership for Lab Oversight &amp; Validation<br>4410 Halvering Campus Drive, Brightmoor, KS 66010-4410</p>
    <p>General Email: <span class="accent">plov@halvering-example.edu</span></p>
    <p>Main Phone Line: <span class="accent">555.014.2290</span></p>
    <p>Fax: <span class="accent">555.014.229</span></p>
    <p><span class="accent">www.plovsite-example.org</span></p>
  </section>
</main>
</body>
</html>
```